Corporate Branding - Web and Print

A UK based company will like to use an existing logo to create branding materials for all marketing related documents, including business card, prints, letterhead, Website, Twitter, Facebook, Instagram logo etc. This company serves high-end clientele in the fashion, health and wellness and as such high quality and class is of utmost importance.
Where the logo can be modernised without losing its character then experiment. The main thing is to have a corporate branding which can be used later for brochures, Business Plan infographics.
The prominent colour within the organisation is burnt orange with no secondary colour. However if you believe a secondary colour is needed then use it, otherwise keep it simple and classy. Any chosen colours have to match perfectly.
Target Market(s)
High net worth individuals
Industry/Entity Type
Health And Wellness
Contact Information for Business Card
classy
Look and feel
Each slider illustrates characteristics of the customer's brand and the style your logo design should communicate.

```html
<!DOCTYPE html>
<html lang="en">
<head>
<meta charset="utf-8">
<title>Velmora Business Card</title>
<link href="https://fonts.googleapis.com/css2?family=Montserrat:wght@800&family=Roboto:wght@400;700&display=swap" rel="stylesheet">
<style>
  :root {
    --stage: #2a2a2a;
    --card: #1b1b1b;
    --card-pattern: #222222;
    --orange: #f39323;
    --shadow: rgba(0,0,0,0.55);
  }
  * { margin: 0; padding: 0; box-sizing: border-box; }
  html, body {
    width: 1200px; height: 852px; overflow: hidden;
    background: var(--stage);
  }
  .stage { position: relative; width: 1200px; height: 852px; }

  .card {
    position: absolute;
    width: 500px; height: 286px;
    border-radius: 16px;
    background: var(--card);
    box-shadow: 0 14px 30px var(--shadow);
    overflow: hidden;
    color: var(--orange);
  }
  .card--back { left: 110px; top: 140px; }
  .card--front { left: 590px; top: 420px; }

  .card__pattern {
    position: absolute; inset: 0;
    background: var(--card-pattern);
  }

  .brand {
    display: flex; flex-direction: column; align-items: center;
    gap: 8px;
  }
  .brand__dot {
    width: 34px; height: 34px; border-radius: 50%;
    background: var(--orange);
  }
  .brand__name {
    font-family: "Montserrat", sans-serif;
    font-weight: 800;
    font-size: 40px;
    letter-spacing: 1px;
    color: var(--orange);
    line-height: 1;
  }
  .card--back .brand {
    position: absolute; left: 0; right: 0; top: 92px;
  }
  .card--front .brand {
    position: absolute; right: 40px; top: 30px;
  }
  .card--front .brand__name { font-size: 36px; }

  .rule {
    position: absolute; height: 1.5px; background: var(--orange);
  }
  .rule--top { left: 30px; right: 30px; top: 140px; }
  .rule--bottom { left: 30px; width: 150px; top: 200px; }

  .person {
    position: absolute; left: 30px; top: 104px;
    font-family: "Roboto", sans-serif; font-weight: 700;
  }
  .person__name { font-size: 15px; letter-spacing: 0.3px; }
  .person__title { font-size: 10px; letter-spacing: 0.3px; }

  .address {
    position: absolute; right: 30px; top: 150px;
    text-align: right;
    font-family: "Roboto", sans-serif; font-size: 11px; line-height: 1.45;
  }

  .contacts {
    position: absolute; left: 30px; top: 208px;
    list-style: none;
    font-family: "Roboto", sans-serif; font-size: 12px; line-height: 1.4;
  }
  .contacts li { display: flex; align-items: center; gap: 10px; }
  .contacts svg { width: 11px; height: 11px; fill: var(--orange); flex: none; }
</style>
</head>
<body>
<main class="stage">
  <section class="card card--back">
    <div class="card__pattern" role="img" aria-label="Faint repeating brand-symbol pattern in dark grey"></div>
    <div class="brand">
      <span class="brand__dot"></span>
      <span class="brand__name">VELMORA</span>
    </div>
  </section>

  <section class="card card--front">
    <div class="brand">
      <span class="brand__dot"></span>
      <span class="brand__name">VELMORA</span>
    </div>
    <div class="person">
      <p class="person__name">AARON HALE</p>
      <p class="person__title">MANAGING DIRECTOR</p>
    </div>
    <div class="rule rule--top"></div>
    <address class="address" style="font-style:normal">
      2207 N. Harbor Rd<br>P.O. Box 4410<br>Fairbrook, Utah 84000
    </address>
    <div class="rule rule--bottom"></div>
    <ul class="contacts">
      <li>
        <svg viewBox="0 0 12 12"><path d="M3 0h6a1 1 0 0 1 1 1v10a1 1 0 0 1-1 1H3a1 1 0 0 1-1-1V1a1 1 0 0 1 1-1zm0 1.5v8h6v-8z"/></svg>
        (555) 310-2274
      </li>
      <li>
        <svg viewBox="0 0 12 12"><path d="M2.5 0.5l2 2.6-1.2 1.4a7 7 0 0 0 4.2 4.2l1.4-1.2 2.6 2-1.3 2A10 10 0 0 1 0.5 1.8z"/></svg>
        (555) 310-2275
      </li>
      <li>
        <svg viewBox="0 0 12 12"><path d="M0 2h12v8H0zm1 1v.4l5 3.2 5-3.2V3z"/></svg>
        info@velmora.com
      </li>
      <li>
        <svg viewBox="0 0 12 12"><path d="M6 0a6 6 0 1 0 0 12A6 6 0 0 0 6 0zm0 1a5 5 0 0 1 1.6 .3C7.2 2 7 3.4 7 5H5c0-1.6-.2-3-.6-3.7A5 5 0 0 1 6 1zM1 6.5h2.9c0 1.4.3 2.7.7 3.5A5 5 0 0 1 1 6.5zm0-1A5 5 0 0 1 3.6 2C3.2 2.8 3 4 3 5.5zm8 0C9 4 8.8 2.8 8.4 2A5 5 0 0 1 11 5.5zm2 1A5 5 0 0 1 7.4 10c.4-.8.7-2.1.7-3.5z"/></svg>
        www.velmora.com
      </li>
    </ul>
  </section>
</main>
</body>
</html>
```